Glint - Advanced Laser Teeth Whitening

Glint is a new teeth whitening business in a market that is not familar which this treatment.
The brochure needs to establish the brand (see logo) and be informative (see copy).
The service will be carried out at a home based clinic and a mobile service will also be available.
I've also attached some stock photos, please feel free to use these and the logo as you think appropriate.
Although many customers will be women, we want the style to also be accessable to men.
Reason: I'm going on business for the next few days so I am extending the deadline so that I can provide proper feedback.
Target Market(s)
All men and women over 18 and particularly women aged between 18 and 40.
Industry/Entity Type
Clinic
Requirements
Must have
- Logo - I have other formats if required - Please e-mail me - peterholm@manx.netPhotos - I would like more photos that the ones attached, I have more please e-mail me.Uncluttered informative copyThe basic price on the front pageContact details on the back page'Copyright 2008 All Rights Reserved' on the back page
Nice to have
- Lots of white to reflect the business and it's clean, proffessional image.
Should not have
- An old fashioned, cluttered or unprofessional apprearance.

```html
<!DOCTYPE html>
<html lang="en">
<head>
<meta charset="utf-8">
<title>Glint – Advanced Laser Teeth Whitening Brochure</title>
<link href="https://fonts.googleapis.com/css2?family=Source+Sans+3:wght@300;400;600&display=swap" rel="stylesheet">
<style>
  :root {
    --backdrop: #f2d3c3;
    --paper: #ffffff;
    --peach: #efcbb6;
    --peach-soft: #f7e3d7;
    --ink: #5a5a5a;
    --ink-dark: #3d3d3d;
    --accent: #e5127d;
    --box-line: #b9b3cf;
  }
  * { box-sizing: border-box; margin: 0; padding: 0; }
  html, body { width: 1200px; height: 900px; overflow: hidden; }
  body {
    background: var(--backdrop);
    font-family: "Source Sans 3", Arial, sans-serif;
    font-weight: 300;
    color: var(--ink);
    position: relative;
  }
  .spread {
    position: absolute; left: 50px; top: 62px; width: 1100px; height: 776px;
    background: var(--paper);
    box-shadow: 4px 5px 6px rgba(0,0,0,0.35);
    overflow: hidden;
  }
  .fold { position: absolute; top: 0; height: 100%; width: 50px; pointer-events: none; }
  .fold-left { left: 370px; background: linear-gradient(90deg, rgba(0,0,0,0.07), rgba(0,0,0,0) 80%); }
  .fold-right { left: 690px; background: linear-gradient(90deg, rgba(0,0,0,0) 20%, rgba(0,0,0,0.06) 100%); }

  .photo { position: absolute; }
  .photo-couple {
    left: 0; top: 0; width: 400px; height: 400px;
    background: radial-gradient(ellipse at 40% 40%, #e2b9a1 0%, #e8c8b5 45%, #f6ece6 72%, #ffffff 100%);
  }
  .smile-band {
    left: 406px; top: 318px; width: 656px; height: 174px;
    background: radial-gradient(ellipse at 50% 50%, #f6f3ef 0%, #f1e6e2 45%, #e6b7b6 80%, #dea3a5 100%);
  }
  .stand-light {
    left: 1010px; top: 8px; width: 70px; height: 180px;
    background: linear-gradient(180deg, #c2ced6 0%, #e3e6e8 100%);
    border-radius: 6px;
  }
  .device-ring {
    position: absolute; left: 30px; top: 600px; width: 135px; height: 135px;
    border-radius: 50%; border: 6px solid var(--peach);
    background: radial-gradient(circle at 50% 55%, #dcecf4 0%, #b9c4ca 55%, #ececec 100%);
  }

  .headline-ring {
    position: absolute; left: 170px; top: 223px; width: 210px; height: 210px;
    border-radius: 50%; border: 8px solid var(--peach); background: var(--paper);
    display: flex; align-items: center; justify-content: center; text-align: center;
    font-size: 19px; line-height: 23px; color: var(--ink-dark);
  }
  .brand-word { color: var(--accent); font-weight: 600; }

  .intro {
    position: absolute; left: 53px; top: 444px;
    font-size: 10.5px; line-height: 17px; white-space: nowrap;
  }
  .intro p { margin-bottom: 7px; }
  .intro .line { display: block; }

  .guide-title {
    position: absolute; left: 440px; top: 18px; width: 580px; text-align: center;
    font-size: 19px; font-weight: 300; color: var(--ink-dark);
  }

  .step {
    position: absolute; background: var(--paper);
    border: 1px solid var(--box-line); border-radius: 14px;
    box-shadow: 2px 3px 4px rgba(0,0,0,0.15);
    font-size: 10.5px; line-height: 17px; white-space: nowrap;
    padding: 12px 10px 0 23px;
  }
  .step-badge { position: absolute; width: 40px; height: 40px; border-radius: 50%; background: var(--peach-soft); }
  .step-badge .num {
    position: absolute; left: 15px; top: -1px; font-size: 34px; font-weight: 600;
    color: var(--peach); line-height: 40px;
  }
  .step-badge .label { position: absolute; left: 2px; top: 5px; font-size: 10px; color: var(--ink); }

  .thumb { position: absolute; }
</style>
</head>
<body>
  <main class="spread">
    <div class="photo photo-couple" role="img" aria-label="Photo of a smiling young couple, cheek to cheek"></div>

    <div class="headline-ring">
      <p>With <span class="brand-word">Glint</span><br>you can have the<br>smile you always<br>wanted in just<br>one session.</p>
    </div>

    <section class="intro">
      <p>Glint uses some of the USA's most advanced teeth<br>whitening technology and gels available to achieve the best<br>results possible for you.</p>
      <p>Glint is the Isle of Man's teeth whitening specialists with<br>a clinic in Glenmarrow and the ability to carry out treatments<br>anywhere in the island.</p>
      <p>The Glint service has been designed with patient safety<br>and comfort in mind and all Glint teeth whitening
        <span class="line" style="padding-left:85px">technicians are trained by leading</span>
        <span class="line" style="padding-left:103px">specialists in the USA.</span></p>
      <p><span class="line" style="padding-left:115px">The Lumora 2400 teeth whitening</span>
        <span class="line" style="padding-left:119px">light used by Glint produces</span>
        <span class="line" style="padding-left:117px">cold blue light that will whiten</span>
        <span class="line" style="padding-left:119px">your teeth between 4 to</span>
        <span class="line" style="padding-left:112px">13 shades.</span></p>
    </section>

    <div class="device-ring" role="img" aria-label="Photo of the Lumora 2400 whitening light head"></div>

    <h1 class="guide-title">The Glint Service – A step by step guide.</h1>

    <div class="photo stand-light" role="img" aria-label="Photo of the laser accelerator on a wheeled stand"></div>

    <div class="step-badge" style="left:398px;top:63px"><span class="num">1</span><span class="label">Step</span></div>
    <div class="step" style="left:432px;top:69px;width:270px;height:97px">
      A fully trained Glint teeth whitening technician<br>will explain the teeth whitening process to you<br>in detail, talk to you about your expectations and<br>answer any questions you may have.
    </div>

    <div class="step-badge" style="left:398px;top:185px"><span class="num">2</span><span class="label">Step</span></div>
    <div class="step" style="left:432px;top:186px;width:270px;height:104px">
      Your pre-treatment tooth shade will be taken<br>using a shade guide and recorded.
    </div>
    <div class="thumb" style="left:515px;top:246px;width:188px;height:50px;background:linear-gradient(90deg,#f4f2ec,#e6dfc9);border-radius:3px" role="img" aria-label="Photo of a tooth shade guide"></div>

    <div class="step-badge" style="left:756px;top:63px"><span class="num">5</span><span class="label">Step</span></div>
    <div class="step" style="left:790px;top:69px;width:270px;height:97px">
      The Lumora 2400 laser accelerator is placed in<br>front of your mouth for 15-20 minutes, this<br>step is then repeated in three cycles.
    </div>

    <div class="step-badge" style="left:756px;top:185px"><span class="num">6</span><span class="label">Step</span></div>
    <div class="step" style="left:790px;top:193px;width:272px;height:97px;padding-left:134px;padding-top:11px">
      Your new shade is<br>revealed to you and the<br>results compared with<br>the old colour.
    </div>
    <div class="thumb" style="left:812px;top:206px;width:98px;height:67px;background:linear-gradient(180deg,#d9b4aa,#efe4dc)" role="img" aria-label="Photo of teeth showing the new shade"></div>

    <div class="photo smile-band" role="img" aria-label="Close-up photo of a smile with bright white teeth"></div>

    <div class="step-badge" style="left:398px;top:512px"><span class="num">3</span><span class="label">Step</span></div>
    <div class="step" style="left:432px;top:515px;width:270px;height:63px;padding-top:13px">
      A cheek retractor is placed into your mouth and<br>you will be asked to wear protective goggles.
    </div>
    <div class="thumb" style="left:615px;top:565px;width:58px;height:50px;background:radial-gradient(circle,#b8c3da,#dfe4ee);border-radius:8px" role="img" aria-label="Photo of a cheek retractor"></div>

    <div class="step-badge" style="left:398px;top:628px"><span class="num">4</span><span class="label">Step</span></div>
    <div class="step" style="left:432px;top:635px;width:270px;height:98px">
      Teeth whitening gel is applied to your upper and<br>lower teeth, covering the surface of each tooth.
    </div>
    <div class="thumb" style="left:500px;top:694px;width:190px;height:52px;background:linear-gradient(180deg,#e4e4e4,#c9c9c9);border-radius:6px" role="img" aria-label="Photo of a whitening gel pen"></div>

    <div class="step-badge" style="left:756px;top:512px"><span class="num">7</span><span class="label">Step</span></div>
    <div class="step" style="left:790px;top:517px;width:272px;height:126px">
      Your Glint teeth whitening technician will give<br>you advice on aftercare and aftercare notes to<br>take away with you.
    </div>
    <div class="thumb" style="left:910px;top:568px;width:138px;height:72px;background:linear-gradient(135deg,#dcebf4,#c3cfe0);border-radius:4px" role="img" aria-label="Photo of an aftercare kit"></div>

    <div class="step-badge" style="left:756px;top:672px"><span class="num">8</span><span class="label">Step</span></div>
    <div class="step" style="left:790px;top:679px;width:272px;height:54px;padding-top:11px">
      Go home and enjoy your new white bright smile.
    </div>

    <div class="fold fold-left"></div>
    <div class="fold fold-right"></div>
  </main>
</body>
</html>
```